VELMO business card - High end Italian floors and coverings

We need a new design for our business card. We are an exclusive company located in Mexico.
Our commercial name is VELMO. Our legal name is Bruma Ceniza SA de CV.
We bring the latest trends in materials for floors and walls such as natural stones, wood, leather, design porcelanato tiles and so.
Our company image colors are black, white and red.
Our customers are high end architects and designers.
We are looking for an elegant but fresh design which reflects exclusivity, simplicity and reliability.
(we are working also in a new website)

Requirements
Nice to have
• back and front design
Space for 2 addresses (one for each showroom location)

```html
<!DOCTYPE html>
<html lang="en">
<head>
<meta charset="utf-8">
<title>VELMO business card</title>
<link rel="stylesheet" href="https://fonts.googleapis.com/css2?family=Questrial&display=swap">
<style>
  :root {
    --page: #d9d9d9;
    --ink: #0f0f0f;
    --ink-soft: #1c1c1c;
    --sheen: #6e6e6e;
    --paper: #f4f4f4;
    --paper-shade: #dcdcdc;
    --white: #ffffff;
    --grey-text: #3a3a3a;
  }
  * { box-sizing: border-box; margin: 0; padding: 0; }
  html, body { width: 1200px; height: 900px; overflow: hidden; }
  body {
    background: var(--page);
    font-family: "Questrial", "Helvetica Neue", Arial, sans-serif;
    display: grid;
    grid-template-columns: 500px 500px;
    grid-template-rows: 286px 286px;
    gap: 70px 60px;
    justify-content: center;
    align-content: center;
  }
  .card {
    position: relative;
    width: 500px;
    height: 286px;
    overflow: hidden;
    box-shadow: 0 10px 24px rgba(0,0,0,.28);
  }
  .card--front {
    background:
      linear-gradient(125deg, var(--ink) 0%, var(--ink) 40%, var(--sheen) 47%, #3a3a3a 60%, var(--ink-soft) 100%);
    color: var(--white);
  }
  .card--back-dark {
    background:
      linear-gradient(90deg, var(--ink) 0%, var(--ink) 14%, #5a5a5a 19%, #2a2a2a 30%, var(--ink) 45%);
    color: var(--white);
  }
  .card--back-light {
    background:
      linear-gradient(90deg, var(--paper-shade) 0%, var(--paper-shade) 14%, var(--white) 19%, var(--paper) 45%);
    color: var(--ink);
  }
  .legal-name {
    position: absolute;
    font-size: 21px;
    line-height: 1.12;
  }
  .brand-name {
    position: absolute;
    font-size: 40px;
    letter-spacing: 1px;
  }
  .card--front .legal-name { top: 28px; left: 30px; }
  .card--front .brand-name { right: 30px; bottom: 26px; }
  .card--front-alt .brand-name { top: 24px; left: 30px; right: auto; bottom: auto; }
  .card--front-alt .legal-name { right: 30px; bottom: 26px; top: auto; left: auto; text-align: right; }

  .back-layout {
    position: absolute;
    left: 130px; right: 30px; top: 34px; bottom: 30px;
    display: grid;
    grid-template-columns: 1fr 1fr;
    gap: 24px;
  }
  .person-name { font-size: 20px; font-weight: 700; }
  .person-role { font-size: 11px; opacity: .8; margin-bottom: 18px; }
  .body-copy { font-size: 11px; line-height: 1.45; margin-bottom: 12px; }
  .card--back-light .body-copy { color: var(--grey-text); }
  .contact { font-size: 11px; line-height: 1.6; }
  .back-brand {
    position: absolute;
    right: 30px; top: 24px;
    font-size: 22px;
    letter-spacing: 1px;
  }
</style>
</head>
<body>
  <section class="card card--front" aria-label="Card front">
    <p class="legal-name">Bruma<br>Ceniza SA<br>de CV</p>
    <p class="brand-name">VELMO</p>
  </section>

  <section class="card card--back-dark" aria-label="Card back, dark">
    <p class="back-brand">VELMO</p>
    <div class="back-layout">
      <div>
        <p class="person-name">Your Name</p>
        <p class="person-role">position</p>
        <p class="body-copy">Lorem ipsum dolor sit amet, consectetur adipiscing elit. Praesent vitae nibh sit amet lorem accumsan blandit. Sed purus justo, volutpat ac ultrices nec, facilisis venenatis est.</p>
      </div>
      <div>
        <p class="body-copy" style="margin-top:60px">Pellentesque imperdiet lectus tortor, sed faucibus massa tincidunt eu.</p>
        <p class="contact">000-111-222<br>info@velmo.mx</p>
      </div>
    </div>
  </section>

  <section class="card card--front card--front-alt" aria-label="Card front, alternate">
    <p class="brand-name">VELMO</p>
    <p class="legal-name">Bruma<br>Ceniza SA<br>de CV</p>
  </section>

  <section class="card card--back-light" aria-label="Card back, light">
    <p class="back-brand">VELMO</p>
    <div class="back-layout">
      <div>
        <p class="person-name">Your Name</p>
        <p class="person-role">position</p>
        <p class="body-copy">Lorem ipsum dolor sit amet, consectetur adipiscing elit. Praesent vitae nibh sit amet lorem accumsan blandit. Sed purus justo, volutpat ac ultrices nec, facilisis venenatis est.</p>
      </div>
      <div>
        <p class="body-copy" style="margin-top:60px">Pellentesque imperdiet lectus tortor, sed faucibus massa tincidunt eu.</p>
        <p class="contact">000-111-222<br>info@velmo.mx</p>
      </div>
    </div>
  </section>
</body>
</html>
```